design a web site for equipment and software pos company

We would a web site similar to the site we whited labed our rbts system .https://tryvelko.com/
website would be on RbTillSystems.com
we would a contact page
877-555-0148

We do not want an exact copy just something similar .
we are tablet po system

we are at

we are selling hardware and software

rb till systems
41 cedar hollow ln
warren, nj 07059
we are cloud based system

Target Market(s)

any retail merchant

Industry/Entity Type

credit card processing in POS asystems

Coding

Coded - Design and coding required

Number of Pages Required

5+ page

Requirements
Must have
• be able to connect webnarra hosting
Nice to have
• modern looking site
Should not have
• any red

```html
<!DOCTYPE html>
<html lang="en">
<head>
<meta charset="utf-8">
<title>RB Till Systems — Tablet POS for Retail</title>
<link rel="stylesheet" href="https://fonts.googleapis.com/css2?family=Lato:wght@400;700&family=Sarabun:wght@500;600&family=Arimo:wght@600;700&display=swap">
<style>
:root{
  --navy:#061521;
  --navy-deep:#03101a;
  --yellow:#f5c518;
  --cream:#fde9a3;
  --ink:#111111;
  --footer:#141414;
  --muted:#9a9a9a;
  --white:#ffffff;
  --coral:#f08a7e;
  --teal:#4fc3d4;
  --mustard:#d6b100;
}
*{margin:0;padding:0;box-sizing:border-box}
html,body{width:1200px;height:900px;overflow:hidden;background:var(--white)}
body{font-family:"Lato",sans-serif;color:var(--ink);position:relative}
.page{position:absolute;left:471px;top:19px;width:474px;height:1589px;transform:scale(.5425);transform-origin:0 0;box-shadow:0 0 0 1px #e2e2e2}
section,header,footer{position:relative;width:474px;overflow:hidden}
.abs{position:absolute}

/* hero */
.hero{height:337px;background:var(--navy)}
.brand{left:18px;top:10px;font-family:"Lato",sans-serif;font-size:9px;font-weight:700;color:var(--white);line-height:18px}
.nav{right:96px;top:16px;display:flex;gap:27px;font-size:6px;color:var(--white)}
.btn-contact{left:410px;top:11px;width:46px;height:17px;background:var(--yellow);font-size:6px;color:var(--ink);display:flex;align-items:center;justify-content:center;border-radius:1px}
.hero-photo{left:18px;top:38px;width:438px;height:289px;border-radius:6px;background:radial-gradient(ellipse at 70% 40%,#6a5744 0%,#3c3228 35%,#1b1a18 70%,#0c0f12 100%)}
.hero-photo::after{content:"";position:absolute;inset:0;border-radius:6px;background:linear-gradient(90deg,rgba(6,21,33,.75) 0%,rgba(6,21,33,.2) 55%,rgba(0,0,0,0) 100%)}
.hero-title{left:33px;top:102px;font-family:"Sarabun",sans-serif;font-weight:600;font-size:21px;line-height:30px;color:var(--white);letter-spacing:.3px;white-space:nowrap}
.hero-title em{font-style:normal;color:var(--yellow)}
.hero-copy{left:34px;top:193px;width:160px;font-size:6.6px;line-height:11px;color:#e4e4e4;font-family:"Sarabun",sans-serif}
.btn-yellow{background:var(--yellow);color:var(--ink);font-size:7px;font-weight:700;display:flex;align-items:center;justify-content:center;border-radius:1px}
.hero .btn-yellow{left:34px;top:248px;width:92px;height:17px}

/* about */
.about{height:240px;background:var(--white)}
.about-title{left:33px;top:65px;font-family:"Arimo",sans-serif;font-weight:700;font-size:13px;line-height:16.5px;color:var(--ink)}
.about-rule{left:33px;top:100px;width:85px;height:1px;background:var(--yellow)}
.about-copy{left:33px;top:110px;width:204px;font-size:7.4px;line-height:13.2px}
.about-photo{left:277px;top:53px;width:179px;height:135px;background:linear-gradient(135deg,#1e2530 0%,#4a3d34 40%,#7e6a55 65%,#2b3a4c 100%)}

/* offer */
.offer{height:221px;background:var(--navy-deep)}
.offer-title{left:0;width:474px;top:52px;text-align:center;font-family:"Arimo",sans-serif;font-weight:600;font-size:20px;color:var(--white)}
.feature{top:92px;width:120px;color:var(--white)}
.feature .line{position:absolute;left:0;top:9px;width:18px;height:1px;background:#bfc6cc}
.feature .dot{position:absolute;left:10px;top:0;width:19px;height:19px;border-radius:50%}
.feature h3{position:relative;margin-left:19px;padding-top:4px;font-size:8px;font-weight:400;line-height:13px}
.feature p{margin-left:19px;margin-top:4px;font-size:7.2px;line-height:11.6px;color:#e0e0e0}

/* future */
.future{height:263px;background:var(--white)}
.future-art{left:240px;top:50px;width:220px;height:163px;border-radius:10px;background:radial-gradient(ellipse at 50% 45%,#c9cff8 0%,#e6e9fc 50%,#ffffff 80%)}
.future-title{left:27px;top:74px;font-family:"Arimo",sans-serif;font-weight:700;font-size:20px;line-height:19.5px;white-space:nowrap;z-index:1}
.future-copy{left:29px;top:124px;width:150px;font-size:7.2px;line-height:13.3px;z-index:1}
.btn-outline{left:29px;top:172px;width:63px;height:15px;border:1px solid var(--ink);font-size:6.5px;display:flex;align-items:center;justify-content:center;border-radius:1px}

/* unlock */
.unlock{height:298px;background:var(--cream)}
.devices{left:0;top:38px;width:170px;height:222px;background:linear-gradient(160deg,#1c1c1c 0%,#3a3a3a 18%,#f2f2f2 22%,#e9efe9 70%,#1c1c1c 100%);border-radius:0 10px 14px 0}
.unlock-title{left:213px;top:80px;font-family:"Arimo",sans-serif;font-weight:600;font-size:15.5px;line-height:23px;white-space:nowrap}
.unlock-copy{left:213px;top:128px;width:200px;font-size:7.2px;line-height:13px}
.try{left:213px;top:166px;font-size:10.5px;font-weight:700}
.try-sub{left:213px;top:181px;font-size:7.2px}
.unlock .btn-yellow{left:213px;top:204px;width:77px;height:16px;border:1px solid #d8a900;font-size:6.5px}

/* footer */
.site-footer{height:230px;background:var(--footer);color:var(--white)}
.site-footer .brand-lg{left:43px;top:43px;font-size:15px;font-weight:700;line-height:32px}
.footer-blurb{left:43px;top:87px;width:108px;font-size:5.6px;line-height:10px;color:#d8d8d8}
.footer-col{top:87px;font-size:6px;line-height:13.2px}
.footer-col h4{font-weight:400;color:var(--muted);font-size:6px}
.subscribe{left:348px;top:87px;display:flex;height:11px}
.subscribe span:first-child{width:56px;background:#5c5c5c;font-size:4px;color:#ccc;padding-left:4px;line-height:11px}
.subscribe span:last-child{width:26px;background:#222;font-size:4px;line-height:11px;text-align:center}
.social{left:378px;top:106px;display:flex;gap:13px}
.social svg{width:8px;height:8px}
</style>
</head>
<body>
<div class="page">

  <section class="hero">
    <div class="abs hero-photo" role="img" aria-label="Photo of a smiling customer paying by card at a café counter"></div>
    <div class="abs brand">RB Till Systems</div>
    <nav class="abs nav">
      <span>Features</span><span>Business Types</span><span>Products</span><span>Partners</span><span>About Us</span>
    </nav>
    <div class="abs btn-contact">Contact</div>
    <h1 class="abs hero-title">Grow Your<br>Business With <em>RB</em><br>Till Systems</h1>
    <p class="abs hero-copy">Lorem ipsum dolor sit amet, consectetur adipiscing elit. Condimentum morbi mauris, ipsum risus a. Semper congue sed sed netus venenatis, ut tellus.</p>
    <a class="abs btn-yellow">Learn more</a>
  </section>

  <section class="about">
    <h2 class="abs about-title">ABOUT<br>RB TILL SYSTEMS</h2>
    <div class="abs about-rule"></div>
    <p class="abs about-copy">Lorem ipsum dolor sit amet, consectetur adipiscing elit. Risus suspendisse elit pretium nulla. Risus arcu vitae tincidunt neque neque nunc adipiscing. Proin non cras interdum placerat dictum amet vel. Vitae dolor, sed tellus egestas.</p>
    <div class="abs about-photo" role="img" aria-label="Photo of a team meeting around a laptop"></div>
  </section>

  <section class="offer">
    <h2 class="abs offer-title">What we offer</h2>
    <div class="abs feature" style="left:33px">
      <span class="line"></span><span class="dot" style="background:var(--coral)"></span>
      <h3>Fully automated and synchronized functionality</h3>
      <p>Lorem ipsum dolor sit amet, consectetur adipiscing elit. Risus suspendisse elit pretium nulla. Risus arcu vitae tincidunt</p>
    </div>
    <div class="abs feature" style="left:176px">
      <span class="line"></span><span class="dot" style="background:var(--mustard)"></span>
      <h3>Deeper business insights reporting</h3>
      <p>Lorem ipsum dolor sit amet, consectetur adipiscing elit. Risus suspendisse elit pretium nulla. Risus arcu vitae tincidunt</p>
    </div>
    <div class="abs feature" style="left:319px">
      <span class="line"></span><span class="dot" style="background:var(--teal)"></span>
      <h3>Openness for integration</h3>
      <p style="margin-top:17px">Lorem ipsum dolor sit amet, consectetur adipiscing elit. Risus suspendisse elit pretium nulla. Risus arcu vitae tincidunt</p>
    </div>
  </section>

  <section class="future">
    <div class="abs future-art" role="img" aria-label="Illustration of two people working beside a large phone showing app screens"></div>
    <h2 class="abs future-title">Make your business<br>future-proof</h2>
    <p class="abs future-copy">Effortlessly sell, manage, report and grow your retail business in every way with RB Till systems.</p>
    <a class="abs btn-outline">Our services</a>
  </section>

  <section class="unlock">
    <div class="abs devices" role="img" aria-label="Tablet and phone showing the sales dashboard"></div>
    <h2 class="abs unlock-title">Unlock your retail super<br>power with RB Till</h2>
    <p class="abs unlock-copy">Contact or chat with our team to find out how RB Till is right for you and your business</p>
    <h3 class="abs try">Try RB Till now</h3>
    <p class="abs try-sub">Discover how easy it is to transform your retail.</p>
    <a class="abs btn-yellow">Contact us now</a>
  </section>

  <footer class="site-footer">
    <div class="abs brand-lg">RB Till Systems</div>
    <p class="abs footer-blurb">We are here for you and your future. Trust us and start growing your business with RB Till systems</p>
    <div class="abs footer-col" style="left:180px">
      <h4>COMPANY</h4><div>About Us</div><div>Features</div><div>Business types</div><div>Products</div>
    </div>
    <div class="abs footer-col" style="left:259px">
      <h4>HELP &amp; SUPPORT</h4><div>Contact Us</div><div>Help center</div><div>FAQs</div>
    </div>
    <div class="abs subscribe"><span>Your email</span><span>Join Us</span></div>
    <div class="abs social">
      <svg viewBox="0 0 8 8"><circle cx="4" cy="4" r="3.3" fill="none" stroke="#fff" stroke-width=".8"/></svg>
      <svg viewBox="0 0 8 8"><rect x=".5" y="1.5" width="7" height="5" fill="#fff"/><path d="M.5 1.5 4 4.5 7.5 1.5" fill="none" stroke="#141414" stroke-width=".7"/></svg>
      <svg viewBox="0 0 8 8"><circle cx="4" cy="4" r="3.5" fill="#fff"/></svg>
    </div>
  </footer>

</div>
</body>
</html>
```